Veterinary Clinic Letterhead - Ridgeview Veterinary Surgery

We need a letterhead design for an established Veterinary Clinic in Brindlewood called Ridgeview Veterinary Surgery. We are a moderate sized mixed animal veterinary clinic offering a wide variety of veterinary services. The design should use the same colour pattern as those in the logos supplied. The design should also include our address (48 Tulloch Road, Brindlewood, Coral Coast, 4917), phone number (07 4158 6734), email (admin@ridgeviewvets.com.au), website (www.ridgeviewvets.com.au) and our opening hours (7am to 6pm Monday to Friday and 9am to 1pm Saturday).
Target Market(s)
Pet owners
Industry/Entity Type
Veterinary
Requirements
Must have
- The logo or modification of it, business address, opening hours, website, phone number and email address

```html
<!DOCTYPE html>
<html lang="en">
<head>
<meta charset="UTF-8">
<title>Ridgeview Veterinary Surgery – Letterhead</title>
<link rel="stylesheet" href="https://fonts.googleapis.com/css2?family=Open+Sans:wght@400;700&display=swap">
<style>
  :root {
    --navy: #0b2a4a;
    --blue-start: #062b50;
    --blue-end: #0a5396;
    --grey-text: #666a6e;
    --grey-rule: #9a9a9a;
    --grey-band: #999999;
    --paper: #ffffff;
    --on-dark: #ffffff;
  }
  * { margin: 0; padding: 0; box-sizing: border-box; }
  html, body {
    width: 848px; height: 1200px; overflow: hidden; background: var(--paper);
  }
  .letterhead {
    position: relative; width: 848px; height: 1200px; overflow: hidden;
    background: var(--paper);
    font-family: "Open Sans", Arial, sans-serif;
  }
  .brand {
    position: absolute; left: 76px; top: 78px;
    display: flex; align-items: center; gap: 12px;
  }
  .brand-dot {
    width: 46px; height: 46px; border-radius: 50%; background: var(--navy); flex: none;
  }
  .brand-name {
    color: var(--navy); font-weight: 700; font-size: 17px; line-height: 1.2;
    text-transform: uppercase; letter-spacing: 0.3px; width: 150px;
  }
  .contact {
    position: absolute; left: 581px; top: 64px; height: 104px;
    border-left: 1.5px solid var(--grey-rule);
    padding-left: 12px; color: var(--grey-text); font-size: 13.5px; line-height: 15.5px;
  }
  .contact-row { display: flex; align-items: flex-start; gap: 6px; }
  .contact-row svg { width: 10px; height: 10px; margin-top: 3px; flex: none; fill: var(--navy); }
  .contact-row.first { margin-top: 6px; }
  .contact-row.address { margin-top: 15px; }
  .footer-band {
    position: absolute; left: 0; bottom: 0; width: 848px; height: 38px;
  }
  .footer-band svg { position: absolute; inset: 0; }
  .opening-hours {
    position: absolute; left: 77px; top: 0; height: 38px; line-height: 38px;
    color: var(--on-dark); font-size: 13.5px; white-space: nowrap;
  }
</style>
</head>
<body>
<div class="letterhead">
  <div class="brand">
    <div class="brand-dot"></div>
    <div class="brand-name">Ridgeview Veterinary Surgery</div>
  </div>

  <div class="contact">
    <div class="contact-row first">
      <svg viewBox="0 0 10 10"><path d="M2 0.5 L3.6 0.3 L4.3 2.6 L3.2 3.4 Q4 5.6 6.4 6.8 L7.3 5.7 L9.6 6.5 L9.4 8.2 Q8.9 9.6 7.5 9.5 Q1 8.4 0.4 2.4 Q0.4 1 2 0.5 Z"/></svg>
      <span>07 4158 6734</span>
    </div>
    <div class="contact-row">
      <svg viewBox="0 0 10 10"><path d="M0 2 H10 V3 L5 6 L0 3 Z M0 4.2 L5 7.2 L10 4.2 V8.5 H0 Z"/></svg>
      <span>admin@ridgeviewvets.com.au</span>
    </div>
    <div class="contact-row">
      <svg viewBox="0 0 10 10"><g fill="none" stroke="#0b2a4a" stroke-width="0.9"><circle cx="5" cy="5" r="4.3"/><ellipse cx="5" cy="5" rx="1.9" ry="4.3"/><path d="M0.7 5 H9.3 M1.5 2.8 H8.5 M1.5 7.2 H8.5"/></g></svg>
      <span>www.ridgeviewvets.com.au</span>
    </div>
    <div class="contact-row address">
      <svg viewBox="0 0 10 10"><path d="M5 0 A3.6 3.6 0 0 1 8.6 3.6 Q8.6 6 5 10 Q1.4 6 1.4 3.6 A3.6 3.6 0 0 1 5 0 Z M5 2.2 A1.4 1.4 0 1 0 5 5 A1.4 1.4 0 1 0 5 2.2 Z"/></svg>
      <span>48 Tulloch Road, Brindlewood<br>Coral Coast, 4917</span>
    </div>
  </div>

  <div class="footer-band">
    <svg width="848" height="38" viewBox="0 0 848 38">
      <defs>
        <linearGradient id="band-blue" x1="0" y1="0" x2="1" y2="0">
          <stop offset="0" stop-color="#062b50"/>
          <stop offset="1" stop-color="#0a5396"/>
        </linearGradient>
      </defs>
      <polygon points="0,0 650,0 621,38 0,38" fill="url(#band-blue)"/>
      <polygon points="660,0 848,0 848,38 631,38" fill="#999999"/>
    </svg>
    <div class="opening-hours">Opening hours: 7am to 6pm Monday to Friday and 9am to 1pm Saturday</div>
  </div>
</div>
</body>
</html>
```